Design Business Card Aerial Drone Photography

we need a business card that shows we are a leader in:
-Aerial Videos
-Aerial Photography
-Aerial Real Estate Photography
the attached logo is in blue, however please feel free to submit creative colors and designs
Updates

I would like to add the words "Veteran Owned and Operated" to my business card Certified Drone Operator should appear as one line Thanks, Ned Corliss

Target Market(s)

real estate, cell towers, companies that want to showcase their company with aerial drone photography

Contact Information for Business Card

logo files have been submitted in pdf, jpg, png, .ai, .eps., .svg formats. Please feel free to be creative with design and colors, possibly a cloud type background
sample attached.
review my website www.brightwrenaerial.example that should help with designing my business card
Services:
-Aerial Videos
-Aerial Photography

Font styles to use
Sans Serif

Colors

Designer to choose colors to be used in the design.

Requirements
Must have
• company logo
• Bright Wren Aerial
• Ned Corliss Certified Drone Operator
• 555-619-4827
• brightwrenaerial@mailbox.example
• www.brightwrenaeriel.example
• 2971 Maplewood Ln, Larkfield GA 30999
Nice to have
• Please feel free to be creative with design and colors

```html
<!DOCTYPE html>
<html lang="en">
<head>
<meta charset="utf-8">
<title>Bright Wren Aerial — Business Card</title>
<link rel="stylesheet" href="https://fonts.googleapis.com/css2?family=Raleway:wght@400;500;700;800&display=swap">
<style>
  :root {
    --brand-blue: #1c6fbd;
    --charcoal: #2e2f31;
    --ink: #2b2b2b;
    --paper: #ffffff;
    --stage: #3a3d41;
    --stroke-light: #ffffff;
    --band-text: #e8e8e8;
  }
  * { box-sizing: border-box; margin: 0; padding: 0; }
  html, body { width: 1200px; height: 900px; overflow: hidden; }
  body {
    background: var(--stage);
    font-family: "Raleway", Arial, sans-serif;
    position: relative;
  }
  .card {
    position: absolute;
    width: 520px;
    height: 297px;
    top: 302px;
    border-radius: 4px;
    overflow: hidden;
  }
  .card--front { left: 50px; background: var(--paper); }
  .card--back { left: 630px; background: var(--brand-blue); }

  /* front */
  .brand-lockup {
    position: absolute; left: 30px; top: 30px;
    display: flex; align-items: center; gap: 10px;
  }
  .brand-lockup__dot {
    width: 16px; height: 16px; border-radius: 50%;
    background: var(--brand-blue);
  }
  .brand-lockup__name {
    color: var(--brand-blue); font-weight: 800; font-size: 22px;
    letter-spacing: 0.5px; text-transform: uppercase;
  }
  .owner { position: absolute; left: 30px; top: 88px; }
  .owner__name {
    color: var(--brand-blue); font-weight: 800; font-size: 19px;
    text-transform: uppercase; letter-spacing: 0.3px;
  }
  .owner__title { color: var(--ink); font-size: 14px; font-weight: 500; margin-top: 3px; }
  .contact-list { position: absolute; left: 30px; top: 148px; list-style: none; }
  .contact-list li {
    display: flex; align-items: center; gap: 8px;
    font-size: 12.5px; color: var(--ink); margin-bottom: 6px;
  }
  .contact-list svg { width: 12px; height: 12px; flex: none; }
  .tagline {
    position: absolute; right: 30px; bottom: 16px;
    color: var(--ink); font-size: 15px; font-weight: 500;
  }
  .front-band { position: absolute; left: 0; bottom: 0; width: 520px; height: 40px; }

  /* back */
  .back-art { position: absolute; inset: 0; }
  .back-art text { font-family: "Raleway", Arial, sans-serif; }
</style>
</head>
<body>

<section class="card card--front" aria-label="Business card front">
  <div class="brand-lockup">
    <span class="brand-lockup__dot"></span>
    <span class="brand-lockup__name">Bright Wren Aerial</span>
  </div>

  <div class="owner">
    <p class="owner__name">Ned Corliss</p>
    <p class="owner__title">Certified Drone Operator</p>
  </div>

  <ul class="contact-list">
    <li>
      <svg viewBox="0 0 24 24" aria-hidden="true"><path fill="#1c6fbd" d="M6.6 10.8a15 15 0 0 0 6.6 6.6l2.2-2.2a1 1 0 0 1 1-.25 11.4 11.4 0 0 0 3.6.57 1 1 0 0 1 1 1V20a1 1 0 0 1-1 1A17 17 0 0 1 3 4a1 1 0 0 1 1-1h3.5a1 1 0 0 1 1 1c0 1.25.2 2.45.57 3.57a1 1 0 0 1-.25 1z"/></svg>
      555-619-4827
    </li>
    <li>
      <svg viewBox="0 0 24 24" aria-hidden="true"><path d="M2 5h20v14H2z M4 7l8 6 8-6" fill="none" stroke="#1c6fbd" stroke-width="2.4"/></svg>
      brightwrenaerial@mailbox.example
    </li>
    <li>
      <svg viewBox="0 0 24 24" aria-hidden="true"><circle cx="12" cy="12" r="9.5" fill="none" stroke="#1c6fbd" stroke-width="2.4"/><path d="M2.5 12h19M12 2.5c-5 5-5 14 0 19M12 2.5c5 5 5 14 0 19" fill="none" stroke="#1c6fbd" stroke-width="2"/></svg>
      www.brightwrenaerial.example
    </li>
  </ul>

  <svg class="front-band" viewBox="0 0 520 40" aria-hidden="true">
    <path d="M0 8 H190 L205 22 V40 H0 Z" fill="var(--charcoal)"/>
  </svg>

  <p class="tagline">Veteran Owned and Operated</p>
</section>

<section class="card card--back" aria-label="Business card back">
  <svg class="back-art" viewBox="0 0 520 297">
    <rect x="0" y="238" width="520" height="59" fill="var(--charcoal)"/>
    <path class="cloud" d="M190 222 H460 A45 45 0 0 0 478 138 A48 48 0 0 0 405 75 A80 80 0 0 0 260 55 A55 55 0 0 0 170 95 A45 45 0 0 0 160 180 A32 32 0 0 0 190 222 Z"
          fill="none" stroke="var(--stroke-light)" stroke-width="2"/>
    <text x="222" y="105" fill="#fff" font-size="14" text-anchor="middle">
      <tspan x="222">Aerial</tspan><tspan x="222" dy="17">Photography</tspan>
    </text>
    <text x="345" y="82" fill="#fff" font-size="14" text-anchor="middle">
      <tspan x="345">Aerial</tspan><tspan x="345" dy="17">Real Estate</tspan><tspan x="345" dy="17">Photography</tspan>
    </text>
    <text x="442" y="170" fill="#fff" font-size="14" text-anchor="middle">
      <tspan x="442">Aerial</tspan><tspan x="442" dy="17">Videos</tspan>
    </text>
    <text x="318" y="172" fill="#fff" font-size="13" font-weight="800" text-anchor="middle" letter-spacing="0.5">BRIGHT WREN AERIAL</text>
    <g class="pin" transform="translate(318 218)">
      <path d="M0 18 C-8 8 -8 4 -8 0 A8 8 0 0 1 8 0 C8 4 8 8 0 18 Z" fill="var(--brand-blue)" stroke="#fff" stroke-width="1.6"/>
      <circle cx="0" cy="0" r="3" fill="#fff"/>
    </g>
    <text x="260" y="273" fill="var(--band-text)" font-size="15" font-weight="500" text-anchor="middle">2971 Maplewood Ln, Larkfield GA 30999</text>
  </svg>
</section>

</body>
</html>
```